App Icon Designs

I am creating an app and I need icons for these categories:
Education
Entertainment
Finance
Games
Health & Fitness
Kids
Lifestyle
Medical
Music
Navigation
News
Photo & Video
Social Networking
Sports
Travel
Utilities
Weather
I would like the icon designs to imitate the style of the included picture. I have also included a picture of the buttons the icons should fit in (75 x 75 pixels). The icons should stick the the simple and flat look.
Please keep all icons 75 x 75 pixels, and NOT 90 x 90 pixels.
Prize increased to $230. Please do your best work. If anyone can successfully imitate the design of the picture included, I will be glad to increase the prize by another $100.

```html
<!DOCTYPE html>
<html lang="en">
<head>
<meta charset="utf-8">
<title>App Category Buttons</title>
<link rel="stylesheet" href="https://fonts.googleapis.com/css2?family=Montserrat:wght@300;400&display=swap">
<style>
  :root {
    --canvas: #f1f2f2;
    --edge: #d9dbdb;
    --label: #ffffff;
    --navy: #34495e;
    --green: #00c08b;
    --pink: #ff87e0;
    --red: #ff5a66;
    --yellow: #ffcb2f;
    --teal: #33ccc0;
    --orange: #ff784f;
    --blue: #3498db;
    --purple: #9b59b6;
    --long-shadow: rgba(0, 0, 0, 0.09);
  }
  * { box-sizing: border-box; margin: 0; padding: 0; }
  html, body {
    width: 1200px;
    height: 1000px;
    overflow: hidden;
    background: var(--canvas);
  }
  .category-board {
    position: absolute;
    left: 72px;
    top: 47px;
    display: grid;
    grid-template-columns: 500px 500px;
    grid-auto-rows: 90px;
    column-gap: 60px;
    row-gap: 11px;
    list-style: none;
  }
  .category-button {
    position: relative;
    display: flex;
    align-items: center;
    border-radius: 8px;
    overflow: hidden;
    background: var(--tone);
    box-shadow: 4px 4px 0 var(--edge);
  }
  .category-button::before {
    content: "";
    position: absolute;
    inset: 0;
    background: var(--long-shadow);
    clip-path: polygon(34px 50px, 92px 40px, 150px 95px, 80px 95px);
  }
  .category-icon {
    position: relative;
    flex: none;
    width: 62px;
    height: 62px;
    margin-left: 32px;
    display: grid;
    place-items: center;
  }
  .category-icon svg { width: 64px; height: 64px; overflow: visible; }
  .category-label {
    position: relative;
    margin-left: 50px;
    font-family: "Montserrat", sans-serif;
    font-weight: 300;
    font-size: 34px;
    letter-spacing: 1.1px;
    white-space: nowrap;
    color: var(--label);
  }
  .tone-navy { --tone: var(--navy); }
  .tone-green { --tone: var(--green); }
  .tone-pink { --tone: var(--pink); }
  .tone-red { --tone: var(--red); }
  .tone-yellow { --tone: var(--yellow); }
  .tone-teal { --tone: var(--teal); }
  .tone-orange { --tone: var(--orange); }
  .tone-blue { --tone: var(--blue); }
  .tone-purple { --tone: var(--purple); }
</style>
</head>
<body>
<ul class="category-board">
  <li class="category-button tone-navy">
    <span class="category-icon">
      <svg viewBox="0 0 64 64" role="img" aria-label="Popcorn box icon">
        <circle cx="20" cy="12" r="7" fill="#fff1c2"/>
        <circle cx="31" cy="8" r="8" fill="#ffe9a8"/>
        <circle cx="43" cy="12" r="7" fill="#fff1c2"/>
        <circle cx="26" cy="17" r="6" fill="#ffe9a8"/>
        <circle cx="38" cy="17" r="6" fill="#ffe9a8"/>
        <polygon points="13,20 51,20 47,64 17,64" fill="#ffffff"/>
        <polygon points="13,20 20.6,20 23,64 17,64" fill="#e8353f"/>
        <polygon points="28.2,20 35.8,20 35,64 29,64" fill="#e8353f"/>
        <polygon points="43.4,20 51,20 47,64 41,64" fill="#e8353f"/>
      </svg>
    </span>
    <span class="category-label">entertainment</span>
  </li>
  <li class="category-button tone-navy">
    <span class="category-icon">
      <svg viewBox="0 0 64 64" role="img" aria-label="Newspaper icon">
        <rect x="2" y="10" width="60" height="46" fill="#e9ebeb"/>
        <rect x="2" y="10" width="60" height="5" fill="#cfd3d5"/>
        <rect x="8" y="20" width="18" height="14" fill="#8e9599"/>
        <g fill="#4a5156">
          <rect x="30" y="20" width="26" height="2"/>
          <rect x="30" y="25" width="26" height="2"/>
          <rect x="30" y="30" width="26" height="2"/>
          <rect x="8" y="38" width="48" height="2"/>
          <rect x="8" y="43" width="48" height="2"/>
          <rect x="8" y="48" width="48" height="2"/>
        </g>
      </svg>
    </span>
    <span class="category-label">news</span>
  </li>

  <li class="category-button tone-green">
    <span class="category-icon">
      <svg viewBox="0 0 64 64" role="img" aria-label="Dollar coin icon">
        <circle cx="32" cy="32" r="30" fill="#f5a623"/>
        <circle cx="32" cy="32" r="24" fill="#fcc419"/>
        <text x="32" y="44" text-anchor="middle" font-family="Montserrat, sans-serif" font-size="34" font-weight="400" fill="#e8921a">$</text>
      </svg>
    </span>
    <span class="category-label">finance</span>
  </li>
  <li class="category-button tone-green">
    <span class="category-icon">
      <svg viewBox="0 0 64 64" role="img" aria-label="Photo print icon">
        <rect x="9" y="2" width="46" height="58" fill="#f4f6f6"/>
        <rect x="13" y="6" width="38" height="36" fill="#5aa9e0"/>
        <polygon points="13,42 25,26 35,36 41,30 51,42" fill="#d9935b"/>
        <circle cx="42" cy="14" r="4" fill="#ffffff"/>
        <polyline points="19,51 23,48 27,51 31,48 35,51 39,48 43,51" fill="none" stroke="#4a5156" stroke-width="2"/>
      </svg>
    </span>
    <span class="category-label">lifestyle</span>
  </li>

  <li class="category-button tone-pink">
    <span class="category-icon">
      <svg viewBox="0 0 64 64" role="img" aria-label="Game controller icon">
        <path d="M14 14h36c8 0 13 10 14 24 1 10-4 14-9 12-4-2-7-8-11-10H20c-4 2-7 8-11 10-5 2-10-2-9-12 1-14 6-24 14-24z" fill="#ffffff"/>
        <rect x="13" y="24" width="12" height="4" fill="#8e9599"/>
        <rect x="17" y="20" width="4" height="12" fill="#8e9599"/>
        <circle cx="47" cy="21" r="2.6" fill="#3498db"/>
        <circle cx="42" cy="26" r="2.6" fill="#ff5a66"/>
        <circle cx="52" cy="26" r="2.6" fill="#ffcb2f"/>
        <circle cx="47" cy="31" r="2.6" fill="#00c08b"/>
      </svg>
    </span>
    <span class="category-label">games</span>
  </li>
  <li class="category-button tone-pink">
    <span class="category-icon">
      <svg viewBox="0 0 64 64" role="img" aria-label="Sneaker icon">
        <path d="M34 4h22v46H6c0-6 6-10 14-14 8-4 14-10 14-18z" fill="#3578c8"/>
        <rect x="34" y="4" width="22" height="6" fill="#2a62a6"/>
        <rect x="4" y="48" width="54" height="8" rx="2" fill="#f4f6f6"/>
        <g stroke="#ffffff" stroke-width="2.5">
          <line x1="24" y1="32" x2="30" y2="38"/>
          <line x1="28" y1="26" x2="34" y2="32"/>
          <line x1="31" y1="19" x2="37" y2="25"/>
        </g>
      </svg>
    </span>
    <span class="category-label">kids</span>
  </li>

  <li class="category-button tone-red">
    <span class="category-icon">
      <svg viewBox="0 0 64 64" role="img" aria-label="Medical cross icon">
        <path d="M24 10h16v14h14v16H40v14H24V40H10V24h14z" fill="#ffffff"/>
        <path d="M10 32h44v8H40v14H24V40H10z" fill="#e6e8e8"/>
      </svg>
    </span>
    <span class="category-label">medical</span>
  </li>
  <li class="category-button tone-red">
    <span class="category-icon">
      <svg viewBox="0 0 64 64" role="img" aria-label="Book icon">
        <rect x="16" y="4" width="34" height="56" rx="2" fill="#2f86c8"/>
        <rect x="16" y="4" width="6" height="56" fill="#236ca6"/>
        <rect x="18" y="56" width="32" height="4" fill="#f4f6f6"/>
        <rect x="27" y="14" width="16" height="2.5" fill="#1d4f7a"/>
        <rect x="27" y="20" width="16" height="2.5" fill="#1d4f7a"/>
        <polygon points="20,0 25,0 25,10 22.5,8 20,10" fill="#ffcb2f"/>
      </svg>
    </span>
    <span class="category-label">education</span>
  </li>

  <li class="category-button tone-yellow">
    <span class="category-icon">
      <svg viewBox="0 0 64 64" role="img" aria-label="Music note icon">
        <polygon points="20,12 54,4 54,14 20,22" fill="#b77bd6"/>
        <rect x="20" y="12" width="6" height="40" fill="#b77bd6"/>
        <rect x="48" y="4" width="6" height="42" fill="#b77bd6"/>
        <ellipse cx="16" cy="52" rx="10" ry="8" fill="#b77bd6"/>
        <ellipse cx="44" cy="46" rx="10" ry="8" fill="#b77bd6"/>
      </svg>
    </span>
    <span class="category-label">music</span>
  </li>
  <li class="category-button tone-yellow">
    <span class="category-icon">
      <svg viewBox="0 0 64 64" role="img" aria-label="Camera icon">
        <rect x="44" y="10" width="10" height="6" fill="#333537"/>
        <rect x="2" y="14" width="60" height="40" rx="4" fill="#333537"/>
        <rect x="2" y="44" width="60" height="10" fill="#2a2b2d"/>
        <circle cx="32" cy="34" r="12" fill="#ffffff"/>
        <circle cx="32" cy="34" r="8" fill="#333537"/>
        <circle cx="10" cy="21" r="2.5" fill="#ff5a66"/>
      </svg>
    </span>
    <span class="category-label">photo &amp; video</span>
  </li>

  <li class="category-button tone-teal">
    <span class="category-icon">
      <svg viewBox="0 0 64 64" role="img" aria-label="Compass icon">
        <circle cx="32" cy="32" r="30" fill="#a5abad"/>
        <circle cx="32" cy="32" r="23" fill="#f4f6f6"/>
        <polygon points="44,18 35,35 29,29" fill="#ff5a66"/>
        <polygon points="20,46 29,29 35,35" fill="#8e9599"/>
        <circle cx="32" cy="32" r="2.5" fill="#4a5156"/>
      </svg>
    </span>
    <span class="category-label">navigation</span>
  </li>
  <li class="category-button tone-teal">
    <span class="category-icon">
      <svg viewBox="0 0 64 64" role="img" aria-label="Heart icon">
        <path d="M32 58C14 44 6 35 6 25 6 17 12 12 19 12c6 0 10 3 13 8 3-5 7-8 13-8 7 0 13 5 13 13 0 10-8 19-26 33z" fill="#ff5a66"/>
        <path d="M32 58C14 44 6 35 6 25 6 17 12 12 19 12c-3 4-5 9-5 14 0 12 8 22 18 32z" fill="#e8464f"/>
      </svg>
    </span>
    <span class="category-label">health &amp; fitness</span>
  </li>

  <li class="category-button tone-orange">
    <span class="category-icon">
      <svg viewBox="0 0 64 64" role="img" aria-label="Smartphone icon">
        <rect x="15" y="2" width="34" height="60" rx="5" fill="#ffffff"/>
        <rect x="18" y="10" width="28" height="42" fill="#3a9ee0"/>
        <circle cx="32" cy="57" r="2.5" fill="#d8dcdc"/>
      </svg>
    </span>
    <span class="category-label">social networking</span>
  </li>
  <li class="category-button tone-orange">
    <span class="category-icon">
      <svg viewBox="0 0 64 64" role="img" aria-label="Briefcase icon">
        <path d="M24 14v-6h16v6" fill="none" stroke="#2e3336" stroke-width="4"/>
        <rect x="0" y="14" width="64" height="44" rx="3" fill="#2e3336"/>
        <rect x="0" y="30" width="64" height="2" fill="#24282a"/>
        <rect x="29" y="27" width="6" height="8" fill="#f5b50c"/>
      </svg>
    </span>
    <span class="category-label">business</span>
  </li>

  <li class="category-button tone-blue">
    <span class="category-icon">
      <svg viewBox="0 0 64 64" role="img" aria-label="Basketball icon">
        <circle cx="32" cy="32" r="30" fill="#f26a2e"/>
        <g fill="none" stroke="#2e2a2a" stroke-width="2.5">
          <line x1="2" y1="32" x2="62" y2="32"/>
          <line x1="32" y1="2" x2="32" y2="62"/>
          <path d="M12 10c8 6 12 14 12 22s-4 16-12 22"/>
          <path d="M52 10c-8 6-12 14-12 22s4 16 12 22"/>
        </g>
      </svg>
    </span>
    <span class="category-label">sports</span>
  </li>
  <li class="category-button tone-blue">
    <span class="category-icon">
      <svg viewBox="0 0 64 64" role="img" aria-label="Airplane icon">
        <path d="M30 4c0-3 4-3 4 0v20l28 14v6L34 36v16l8 6v4l-10-3-10 3v-4l8-6V36L2 44v-6l28-14z" fill="#f4f6f6"/>
        <rect x="12" y="36" width="4" height="8" fill="#d8dcdc"/>
        <rect x="48" y="36" width="4" height="8" fill="#d8dcdc"/>
      </svg>
    </span>
    <span class="category-label">travel</span>
  </li>

  <li class="category-button tone-purple">
    <span class="category-icon">
      <svg viewBox="0 0 64 64" role="img" aria-label="Sun behind cloud icon">
        <circle cx="26" cy="26" r="26" fill="#f6b90f"/>
        <circle cx="26" cy="26" r="21" fill="#ffce2e"/>
        <g fill="#ffffff">
          <circle cx="42" cy="46" r="10"/>
          <circle cx="54" cy="52" r="8"/>
          <circle cx="32" cy="54" r="7"/>
          <rect x="30" y="52" width="32" height="10" rx="5"/>
        </g>
      </svg>
    </span>
    <span class="category-label">weather</span>
  </li>
  <li class="category-button tone-purple">
    <span class="category-icon">
      <svg viewBox="0 0 64 64" role="img" aria-label="Wrench icon">
        <path d="M8 4l8 8-2 6-6 2-8-8c-2 8 4 16 12 15l30 30c2 2 6 2 8 0s2-6 0-8L20 19C21 11 14 5 8 4z" fill="#cfd3d5"/>
        <path d="M20 19l30 30c2 2 2 6 0 8l4 0c2-2 2-6 0-8L24 19z" fill="#b4b8ba"/>
      </svg>
    </span>
    <span class="category-label">utilities</span>
  </li>
</ul>
</body>
</html>
```